Amber Tides: Lantern Tales from Seven Winters by the Northern Sea and Other Small Wonders

Good day! I am excited to work again with you, amazing designers! This time I am looking for the cover design of my book.
Dimensions 6” x 9”
The book name is as my name project. I love simplicity, but yet that is impactful. I love colours, I don't have a specific colour in mind, but I like the mustard colour as the one in the logo of my company. I am open to ideas! I have attached some cover samples that I like so that it gives a better idea of what I have on mind.
I am looking for something that looks professional, yet, not super serious, that it's approachable to people. Something that calls their attention at first glance.
I am working with my editor and my interior designer as well to finalize this part of the book. I will be working with the person that I select for the book design to finalize it.
About the book, here a passage of an unedited version of the introduction for guidance :
My intention is to take you on a journey to help you to understand what is going on in your mind so that you get out from anything that is holding you back in your life. My intention is to guide you to start fully living and experiencing a life that your mind even have yet conceived. To experience a life where you live fearless and without suffering. Living your life where you are the navigator and the creator of how you are experiencing it and you are living in a world of possibilities where there are no limitations.
For it, we will start to understand more about the mind and about the brain. I am not a neuroscientist and neither I consider my self an expert in the workings of the brain, what I know is the result of my fascination about our brain. This curiosity and the part of me that likes to understand how things work took me to read, research and learn about how our brain works and how its intrinsic mechanisms are subconsciously influencing and limiting us. I encourage you to stay on this part, it can be a bit technical, but understanding how it works will empower you not to allow your mind to dictate the way you approach your life and to live on autopilot.
We will continue to describe how you have been programmed throughout your life, putting you inside a box limited by your subconscious beliefs and ideas about the world. In this part, we will also discuss what ego is, how it is subconsciously limiting you and how the ways of when ego manifests itself are limiting you and making you suffer. Now that you know how you have been enclosed in your mind for all your life, we will move to discuss how you can get out of it. You will learn how to master your emotions to eliminate your suffering and not allow them to control the direction of your life and use them as a mechanism to get out from your programed mind. We continue to discuss how to leverage the power of your mind and harness your power of choice. Finally, I invite you to see yourself as a holistic being so that you start truly living and take control over the direction of your life, by nourishing and taking care of all those aspects of you utilizing their wisdom and synergy to achieve higher connection within yourself, your soul and live your life in a higher level of consciousness with peace, flow, love and purpose.

```html
<!DOCTYPE html>
<html lang="en">
<head>
<meta charset="utf-8">
<title>Amber Tides — Book Cover</title>
<link rel="stylesheet" href="https://fonts.googleapis.com/css2?family=Noto+Sans:wght@400;600&display=swap">
<style>
  :root {
    --white: #ffffff;
    --mustard: #fbbd16;
    --navy: #1a4f8c;
    --amber-light: #f3c77a;
    --amber: #c98a2a;
    --bronze: #7a4a14;
    --umber: #2e1606;
    --night: #0d0502;
  }
  * { margin: 0; padding: 0; box-sizing: border-box; }
  html, body { width: 908px; height: 1200px; overflow: hidden; background: var(--night); }
  .cover {
    position: relative;
    width: 908px;
    height: 1200px;
    overflow: hidden;
    font-family: "Noto Sans", "DejaVu Sans", Verdana, sans-serif;
  }
  .cover__backdrop {
    position: absolute;
    inset: 0;
    background:
      linear-gradient(to bottom,
        var(--white) 0%,
        var(--white) 13%,
        var(--amber-light) 24%,
        var(--amber) 36%,
        var(--bronze) 52%,
        var(--umber) 72%,
        var(--night) 92%);
  }
  .brand {
    position: absolute;
    left: 196px;
    top: 112px;
    display: flex;
    align-items: center;
    gap: 22px;
  }
  .brand__dot {
    width: 84px;
    height: 84px;
    border-radius: 50%;
    background: var(--navy);
  }
  .brand__name {
    color: var(--mustard);
    font-weight: 600;
    font-size: 44px;
    letter-spacing: 1px;
  }
  .title {
    position: absolute;
    left: 180px;
    right: 30px;
    top: 0;
    bottom: 0;
  }
  .title__line {
    position: absolute;
    left: 0;
    white-space: nowrap;
    line-height: 1;
    font-weight: 400;
  }
  .title__main {
    top: 318px;
    color: var(--white);
    font-size: 104px;
  }
  .title__sub {
    color: var(--mustard);
    font-size: 72px;
  }
  .title__sub small {
    font-size: 36px;
    margin-right: 10px;
  }
  .title__sub--1 { top: 470px; }
  .title__sub--2 { top: 572px; }
  .title__sub--3 { top: 674px; }
  .title__sub--4 { top: 776px; }
  .title__sub--5 { top: 878px; }
</style>
</head>
<body>
  <main class="cover">
    <div class="cover__backdrop" role="img" aria-label="Streaks of falling golden light fading from white at the top to deep brown and black below"></div>

    <header class="brand">
      <span class="brand__dot"></span>
      <span class="brand__name">Lumenfold</span>
    </header>

    <h1 class="title">
      <span class="title__line title__main">Amber Tides</span>
      <span class="title__line title__sub title__sub--1">Lantern Tales</span>
      <span class="title__line title__sub title__sub--2"><small>from</small>Seven Winters</span>
      <span class="title__line title__sub title__sub--3"><small>by the</small>Northern Sea</span>
      <span class="title__line title__sub title__sub--4"><small>and</small>Other Small</span>
      <span class="title__line title__sub title__sub--5">Wonders</span>
    </h1>
  </main>
</body>
</html>
```